Business Card Design Project

i need a bussines car design
Veltra Clinical Hypnotherapy

Gordon Wexley
Psychotherapy & Hypnosis

64029381 /0427956120

back of the card appoinment space.

file was provided on a PDF, LOgo , use the blu colorsa as well , elegant, clear,

Target Market(s)

young professional, caucasian , young mothers.

Industry/Entity Type

Business

```html
<!DOCTYPE html>
<html lang="en">
<head>
<meta charset="utf-8">
<title>Veltra Clinical Hypnotherapy – Business Card</title>
<link rel="stylesheet" href="https://fonts.googleapis.com/css2?family=Open+Sans:ital,wght@0,300;0,400;0,600;0,700;1,400;1,700&display=swap">
<style>
  :root {
    --page: #ebe8e3;
    --card-blue: #0b4a85;
    --card-blue-edge: #083a6a;
    --ink-light: #cfe0f1;
    --ink-soft: #a9c4e0;
    --card-white: #ffffff;
    --ink-navy: #1c2c40;
    --rule-grey: #9aa3ad;
  }
  * { margin: 0; padding: 0; box-sizing: border-box; }
  html, body {
    width: 1200px; height: 880px; overflow: hidden;
    background: var(--page);
    font-family: "Open Sans", Arial, sans-serif;
  }
  .sheet {
    width: 1200px; height: 880px;
    display: flex; align-items: center; justify-content: center; gap: 40px;
  }
  .card {
    position: relative;
    width: 540px; height: 310px;
    border-radius: 26px;
    box-shadow: 0 6px 18px rgba(0,0,0,0.18);
  }

  /* Front */
  .card--front { background: var(--card-blue); color: var(--ink-light); }
  .brand {
    position: absolute; left: 60px; top: 70px; right: 40px;
    display: flex; align-items: center; gap: 22px;
  }
  .brand__dot {
    width: 64px; height: 64px; border-radius: 50%;
    background: var(--ink-soft); flex: none;
  }
  .brand__text { flex: 1; }
  .brand__name {
    font-weight: 300; font-size: 31px; letter-spacing: 0.5px;
    color: var(--ink-light); line-height: 1.1;
    padding-bottom: 5px;
    border-bottom: 1px solid var(--ink-light);
  }
  .brand__web {
    font-size: 12.5px; font-style: italic; letter-spacing: 1.2px;
    color: var(--ink-light); margin-top: 5px;
  }
  .person {
    position: absolute; left: 196px; top: 196px; text-align: center;
  }
  .person__name { font-weight: 700; font-style: italic; font-size: 17px; color: var(--ink-soft); }
  .person__role { font-style: italic; font-size: 12.5px; color: var(--ink-soft); margin-top: 4px; }
  .contact {
    position: absolute; left: 392px; top: 196px;
    list-style: none; font-size: 14px; color: var(--ink-light);
  }
  .contact li { display: flex; align-items: center; gap: 7px; height: 25px; }
  .contact svg { width: 14px; height: 16px; fill: none; stroke: var(--ink-soft); stroke-width: 1.6; }

  /* Back */
  .card--back { background: var(--card-white); color: var(--ink-navy); padding: 30px 34px; }
  .back__title { font-weight: 700; font-size: 13px; letter-spacing: 2.5px; }
  .back__line { font-size: 11.5px; margin-top: 5px; }
  .back__heading { font-weight: 700; font-size: 13px; margin-top: 18px; margin-bottom: 8px; }
  .slots { list-style: none; }
  .slot { display: flex; gap: 10px; align-items: flex-end; height: 24px; }
  .slot span { display: block; border-bottom: 1px solid var(--rule-grey); height: 1px; }
  .slot .w-day { width: 150px; } .slot .w-d { width: 36px; } .slot .w-t { width: 70px; }
  .back__note { position: absolute; right: 30px; bottom: 22px; font-size: 8.5px; color: var(--rule-grey); }
</style>
</head>
<body>
<main class="sheet">
  <section class="card card--front" aria-label="Business card front">
    <div class="brand">
      <div class="brand__dot"></div>
      <div class="brand__text">
        <div class="brand__name">Veltra Hypnotherapy</div>
        <div class="brand__web">www.veltraclinicalhypnotherapy.com.au</div>
      </div>
    </div>
    <div class="person">
      <div class="person__name">Gordon Wexley</div>
      <div class="person__role">Psychotherapy &amp; Hypnosis</div>
    </div>
    <ul class="contact">
      <li>
        <svg viewBox="0 0 14 16"><rect x="3" y="1" width="8" height="14" rx="1.5"/><line x1="6" y1="12.5" x2="8" y2="12.5"/></svg>
        640 29 381
      </li>
      <li>
        <svg viewBox="0 0 14 16"><rect x="1" y="4" width="12" height="11" rx="1"/><rect x="3" y="1" width="3" height="8"/><line x1="8" y1="7" x2="11" y2="7"/><line x1="8" y1="10" x2="11" y2="10"/><line x1="8" y1="13" x2="11" y2="13"/></svg>
        0427 956 120
      </li>
    </ul>
  </section>

  <section class="card card--back" aria-label="Business card back">
    <div class="back__title">Veltra Clinical Hypnotherapy</div>
    <div class="back__line">Appointment. Phone: 0427 956 120</div>
    <div class="back__line">42 Harlow Street, Kensworth 3021</div>
    <div class="back__line">www.veltraclinicalhypnotherapy.com.au</div>
    <div class="back__heading">Appointments</div>
    <ul class="slots">
      <li class="slot"><span class="w-day"></span><span class="w-d"></span><span class="w-d"></span><span class="w-t"></span></li>
      <li class="slot"><span class="w-day"></span><span class="w-d"></span><span class="w-d"></span><span class="w-t"></span></li>
      <li class="slot"><span class="w-day"></span><span class="w-d"></span><span class="w-d"></span><span class="w-t"></span></li>
      <li class="slot"><span class="w-day"></span><span class="w-d"></span><span class="w-d"></span><span class="w-t"></span></li>
    </ul>
    <div class="back__note">Please give 24 hours notice</div>
  </section>
</main>
</body>
</html>
```